We need a postcard design to promote the book written by our founder and president, Rick Tolver. The book is titled KESTRAL: The Craft and Method of Persuasion. We're open to any eye-catching image designs you come up with.

```html
<!DOCTYPE html>
<html lang="en">
<head>
<meta charset="utf-8">
<title>KESTRAL Postcard – Front and Back</title>
<link href="https://fonts.googleapis.com/css2?family=Josefin+Sans:wght@400;600;700&family=Lato:wght@400;700;900&family=Quicksand:wght@500;700&display=swap" rel="stylesheet">
<style>
  :root {
    --bg: #a4a4a4;
    --teal: #86c1b9;
    --teal-mid: #5e8a85;
    --charcoal: #262626;
    --white: #ffffff;
    --olive: #b7bd88;
    --orange: #f6b21d;
    --yellow: #e4e26a;
    --gold-line: #c9b98a;
    --ink: #1f1f1f;
  }
  * { box-sizing: border-box; margin: 0; padding: 0; }
  html, body { width: 1200px; height: 1200px; overflow: hidden; }
  body { background: var(--bg); position: relative; font-family: "Lato", sans-serif; }

  .postcard {
    position: absolute; left: 260px; width: 680px; height: 527px;
    overflow: hidden; box-shadow: 0 10px 24px rgba(0,0,0,.35);
  }
  .postcard--front { top: 46px; background: var(--white); }
  .postcard--back { top: 627px; background: var(--white); }

  /* FRONT */
  .front__hero {
    position: absolute; left: 0; top: 0; width: 100%; height: 430px;
    background: linear-gradient(180deg, var(--teal) 0%, var(--teal-mid) 38%, #3b3f3e 72%, var(--charcoal) 100%);
  }
  .front__title {
    position: absolute; left: 44px; top: 82px;
    font-family: "Lato", sans-serif; font-weight: 900;
    font-size: 70px; line-height: 1; letter-spacing: 4px;
    color: var(--white);
  }
  .front__subtitle {
    position: absolute; left: 46px; top: 190px;
    font-family: "Josefin Sans", sans-serif; font-weight: 600;
    font-size: 22px; color: #1e2423; letter-spacing: .3px;
  }
  .front__subject {
    position: absolute; left: 44px; top: 216px;
    font-family: "Josefin Sans", sans-serif; font-weight: 700;
    font-size: 46px; color: var(--white);
  }
  .front__author {
    position: absolute; left: 46px; top: 308px; width: 274px; height: 80px;
    border: 2px solid var(--gold-line);
    display: flex; align-items: center; justify-content: center;
    font-family: "Quicksand", sans-serif; font-weight: 700;
    font-size: 30px; letter-spacing: 5px; color: var(--white);
  }
  .front__book {
    position: absolute; left: 392px; top: 120px; width: 238px; height: 330px;
    transform: rotate(8deg);
    background: linear-gradient(180deg, #2a2c2c 0%, #3d4a48 55%, #7fb5ad 100%);
    border-right: 12px solid #f2f2f2;
    box-shadow: 6px 10px 18px rgba(0,0,0,.35);
  }
  .front__availability {
    position: absolute; left: 46px; top: 452px;
    display: flex; align-items: baseline; gap: 20px;
  }
  .front__availability-label {
    font-family: "Quicksand", sans-serif; font-weight: 500; font-size: 22px; color: var(--ink);
  }
  .front__retailer {
    font-family: "Quicksand", sans-serif; font-weight: 700; font-size: 28px; color: var(--ink);
  }
  .front__stripe {
    position: absolute; left: 0; bottom: 0; width: 100%; height: 14px; display: flex;
  }
  .front__stripe span { height: 100%; }
  .stripe--olive { background: var(--olive); }
  .stripe--orange { background: var(--orange); }
  .stripe--yellow { background: var(--yellow); }

  /* BACK */
  .back__panel {
    position: absolute; left: 0; top: 0; width: 415px; height: 100%;
    background: linear-gradient(180deg, var(--teal) 0%, var(--teal-mid) 35%, #3a3d3c 70%, var(--charcoal) 100%);
  }
  .back__cover {
    position: absolute; left: 337px; top: 26px; width: 136px; height: 188px;
    background: linear-gradient(180deg, #2a2c2c 0%, #3d4a48 55%, #7fb5ad 100%);
    box-shadow: 0 3px 8px rgba(0,0,0,.3);
  }
  .back__stamp {
    position: absolute; right: 27px; top: 34px; width: 40px; height: 40px;
    border: 1.5px solid var(--ink);
  }
  .back__address { position: absolute; right: 32px; top: 246px; width: 153px; }
  .back__address span { display: block; height: 1px; background: var(--ink); margin-bottom: 21px; }
  .back__letter {
    position: absolute; left: 25px; top: 24px; width: 370px;
    font-size: 12.3px; line-height: 16.2px; color: var(--white); text-align: justify;
  }
  .back__letter p { margin-bottom: 16px; }
  .back__letter .narrow { width: 277px; }
  .back__signature { font-size: 12.3px; }
  .back__signature strong { font-size: 17px; font-weight: 700; }
</style>
</head>
<body>

  <section class="postcard postcard--front" aria-label="Postcard front">
    <div class="front__hero"></div>
    <h1 class="front__title">KESTRAL</h1>
    <p class="front__subtitle">THE CRAFT AND METHOD OF</p>
    <p class="front__subject">PERSUASION</p>
    <p class="front__author">RICK TOLVER</p>
    <div class="front__book" role="img" aria-label="Book cover of KESTRAL: The Craft and Method of Persuasion with orbiting ring illustration"></div>
    <div class="front__availability">
      <span class="front__availability-label">Available at</span>
      <span class="front__retailer">Bookhaven</span>
    </div>
    <div class="front__stripe">
      <span class="stripe--olive" style="width:165px"></span>
      <span class="stripe--orange" style="width:174px"></span>
      <span class="stripe--yellow" style="width:178px"></span>
      <span class="stripe--olive" style="flex:1"></span>
    </div>
  </section>

  <section class="postcard postcard--back" aria-label="Postcard back">
    <div class="back__panel"></div>
    <div class="back__cover" role="img" aria-label="Small book cover of KESTRAL by Rick Tolver"></div>
    <div class="back__stamp"></div>
    <div class="back__address"><span></span><span></span><span></span><span></span></div>
    <div class="back__letter">
      <p class="narrow">We know how difficult training can be in your industry. Unlike children, whose sponge-like minds are ripe for training, you work with adults. Adults have unique opinions and established habits that can make them unruly trainees.</p>
      <p class="narrow">That’s why we’re here. The Tolver Group is a consulting and training organization, and we’ve worked with hundreds of businesses across a dozen industries (including business to business and business to consumer enterprises) to help refine their training and make their business more effective. Businesses experience an average growth of 20% within the first year of working with The Tolver Group.</p>
      <p>We’re the experts on adult behavior change; we know the ins-and-outs of the hows and whys, and we can help you gain that knowledge, too.</p>
      <p>Need proof? That’s why we’ve sent along this copy of KESTRAL: The Craft and Method of Persuasion. In this book I break down the six step process I’ve refined to enact adult behavioral change. It’s a quick and easy read, and I think you’ll enjoy it.</p>
      <p>Once you’ve read KESTRAL, you might be inspired to change your business. When that happens, give us a call. We’d love to help.</p>
      <p class="back__signature"><strong>RICK TOLVER</strong>, Founder &amp; CEO</p>
    </div>
  </section>

</body>
</html>
```